Pharmacy Moving Flyer Design

We are a community pharmacy that is relocating to new premises and as a result changing our name also. Our current name is Bramble Lane Pharmacy and our new name will be Red Kite Pharmacy. I want to include a relocation map and also stress the fact that the only thing changing is the name and the location. Everything else will stay the same but newer!
Current address is 47 Maple Row, Oswestry, SY11 4LN. New address Red Kite Pharmacy, 82 Foxley Parade, Oswestry, SY11 5DT. The phone numbers will remain the same - 01691 738425 and 0800 4538062. The date for opening in our new location is Monday 17th November 2014.

Industry/Entity Type

Pharmacy

```html
<!DOCTYPE html>
<html lang="en">
<head>
<meta charset="utf-8">
<title>We're Moving – Bramble Lane Pharmacy</title>
<link rel="stylesheet" href="https://fonts.googleapis.com/css2?family=Oswald:wght@600&family=Roboto+Condensed:wght@400;700&display=swap">
<style>
  :root {
    --brand-blue: #1f6a8c;
    --brand-navy: #0f3a52;
    --accent-blue: #3a8fb8;
    --ink: #34414b;
    --paper: #ffffff;
  }
  * { margin: 0; padding: 0; box-sizing: border-box; }
  html, body { width: 1200px; height: 850px; overflow: hidden; background: var(--paper); }
  .flyer {
    position: relative;
    width: 1200px;
    height: 850px;
    background: var(--paper);
    font-family: "Roboto Condensed", "Arial Narrow", sans-serif;
    color: var(--ink);
  }
  .headline {
    position: absolute;
    left: 78px;
    top: 118px;
    font-family: "Oswald", "Arial Narrow", sans-serif;
    font-weight: 600;
    font-size: 110px;
    line-height: 1;
    letter-spacing: 3px;
    color: var(--brand-blue);
    white-space: nowrap;
  }
  .subtitle {
    position: absolute;
    left: 88px;
    top: 252px;
    font-size: 30px;
    line-height: 1;
    color: var(--ink);
    white-space: nowrap;
  }
  .subtitle strong { font-weight: 700; }
  .chevrons {
    position: absolute;
    left: 852px;
    top: 141px;
    width: 284px;
    height: 141px;
  }
  .map-note {
    position: absolute;
    left: 916px;
    top: 302px;
    font-size: 21px;
    color: var(--brand-blue);
  }
  .label {
    position: absolute;
    top: 376px;
    display: flex;
    align-items: center;
    gap: 14px;
    font-weight: 700;
    font-size: 27px;
    line-height: 1;
    color: var(--brand-blue);
    text-transform: uppercase;
  }
  .label svg { width: 20px; height: 28px; }
  .label--from { left: 88px; }
  .label--to { left: 612px; }
  .address-band {
    position: absolute;
    left: 0;
    top: 423px;
    width: 1200px;
    height: 134px;
    background: var(--brand-blue);
    color: var(--paper);
  }
  .address {
    position: absolute;
    top: 32px;
    line-height: 1.25;
  }
  .address--from { left: 88px; }
  .address--to { left: 608px; }
  .address__name { font-weight: 700; font-size: 30px; }
  .address__street { font-size: 28px; }
  .tagline {
    position: absolute;
    left: 88px;
    top: 612px;
    font-weight: 700;
    font-size: 35px;
    line-height: 1;
    color: var(--brand-blue);
    white-space: nowrap;
  }
  .opening-band {
    position: absolute;
    left: 0;
    top: 696px;
    width: 1200px;
    height: 154px;
    background: var(--brand-navy);
  }
  .opening-band__label {
    position: absolute;
    left: 80px;
    top: 48px;
    font-weight: 700;
    font-size: 40px;
    line-height: 1;
    color: var(--accent-blue);
    text-transform: uppercase;
  }
  .opening-band__date {
    position: absolute;
    left: 622px;
    top: 46px;
    font-weight: 700;
    font-size: 42px;
    line-height: 1;
    color: var(--paper);
    white-space: nowrap;
  }
</style>
</head>
<body>
<main class="flyer">
  <h1 class="headline">WE’RE MOVING</h1>
  <p class="subtitle"><strong>Bramble Lane Pharmacy</strong> is changing location</p>

  <svg class="chevrons" viewBox="0 0 300 148" preserveAspectRatio="none" aria-hidden="true">
    <g fill="var(--brand-blue)">
      <polygon points="0,0 50,0 124,74 50,148 0,148 74,74"/>
      <polygon points="88,0 138,0 212,74 138,148 88,148 162,74"/>
      <polygon points="176,0 226,0 300,74 226,148 176,148 250,74"/>
    </g>
  </svg>
  <p class="map-note">See back for map</p>

  <div class="label label--from">
    <svg viewBox="0 0 20 28" aria-hidden="true"><path fill="currentColor" d="M10 0C4.5 0 0 4.4 0 9.8 0 17 10 28 10 28s10-11 10-18.2C20 4.4 15.5 0 10 0zm0 14a4.2 4.2 0 1 1 0-8.4 4.2 4.2 0 0 1 0 8.4z"/></svg>
    <span>From</span>
  </div>
  <div class="label label--to">
    <svg viewBox="0 0 20 28" aria-hidden="true"><path fill="currentColor" d="M10 0C4.5 0 0 4.4 0 9.8 0 17 10 28 10 28s10-11 10-18.2C20 4.4 15.5 0 10 0zm0 14a4.2 4.2 0 1 1 0-8.4 4.2 4.2 0 0 1 0 8.4z"/></svg>
    <span>To</span>
  </div>

  <section class="address-band">
    <div class="address address--from">
      <p class="address__name">Bramble Lane Pharmacy</p>
      <p class="address__street">47 Maple Row, Oswestry, SY11 4LN</p>
    </div>
    <div class="address address--to">
      <p class="address__name">Red Kite Pharmacy</p>
      <p class="address__street">82 Foxley Parade, Oswestry, SY11 5DT.</p>
    </div>
  </section>

  <p class="tagline">Same great products, same excellent service, different name and location.</p>

  <section class="opening-band">
    <p class="opening-band__label">Grand Opening</p>
    <p class="opening-band__date">Monday 17th November 2014</p>
  </section>
</main>
</body>
</html>
```